Creative paving postcard front

New postcard front design to acquire paving jobs for next years work season. Background: we are a family owned and operated paving company. We work from march to December paving residential driveways as well as commercial projects. currently we are booked for the rest of this season, but we would like to start lining up work for next season.Goal of this card front: get driveway leads for next season. use creative wording over one of our work photos to make a creative post card front that will generate interest. Specs: Card is 8.5 X 11, the back side of the card that will be used is included in the upload files. Also in the upload files are work photos. Choose whichever photo you think would be best for the post card front. If you want background on our company, check out our facebook page, bellmont paving, or our website, www.bellmontpaving-example.com. open to new creative ideas. PAVE - ITQuestions? send me an email at tomwbellmont@mailbox-example.com
Target Market(s)
homeowners who need new driveways
Industry/Entity Type
Residential Construction
Colors
Designer to choose colors to be used in the design.
Look and feel

```html
<!DOCTYPE html>
<html lang="en">
<head>
<meta charset="utf-8">
<title>Bellmont Paving – Postcard Front</title>
<link href="https://fonts.googleapis.com/css2?family=Oswald:wght@200;700&family=Archivo+Black&family=Roboto+Condensed:wght@400;700&display=swap" rel="stylesheet">
<style>
  :root {
    --sky: #e4ebee;
    --forest: #2f4a22;
    --forest-light: #5b7d3a;
    --house: #e9e6d8;
    --roof: #6d7075;
    --lawn: #7fa544;
    --asphalt: #5b616a;
    --asphalt-dark: #3c4148;
    --frame: #ffffff;
    --accent: #fff200;
    --ink: #111111;
    --brand-red: #c8102e;
  }
  html, body {
    margin: 0;
    padding: 0;
    width: 1200px;
    height: 927px;
    overflow: hidden;
    background: #ffffff;
  }
  .postcard {
    position: relative;
    width: 1200px;
    height: 927px;
    overflow: hidden;
  }
  .hero-photo {
    position: absolute;
    inset: 0;
    background:
      radial-gradient(ellipse 520px 200px at 760px 330px, var(--house) 0%, rgba(233,230,216,0.85) 45%, rgba(233,230,216,0) 100%),
      radial-gradient(ellipse 320px 150px at 1060px 300px, #ddd8c8 0%, rgba(221,216,200,0) 100%),
      radial-gradient(ellipse 320px 130px at 660px 250px, var(--roof) 0%, rgba(109,112,117,0) 100%),
      radial-gradient(ellipse 340px 160px at 1000px 560px, var(--lawn) 0%, rgba(127,165,68,0.7) 55%, rgba(127,165,68,0) 100%),
      radial-gradient(ellipse 120px 120px at 60px 520px, var(--lawn) 0%, rgba(127,165,68,0) 100%),
      radial-gradient(ellipse 110px 170px at 920px 380px, #6b4a9a 0%, rgba(107,74,154,0.5) 50%, rgba(107,74,154,0) 100%),
      radial-gradient(ellipse 560px 500px at 170px 180px, var(--forest) 0%, rgba(47,74,34,0.85) 55%, rgba(47,74,34,0) 100%),
      linear-gradient(180deg, var(--sky) 0%, #cdd8c5 14%, var(--forest-light) 30%, #789a4c 44%, #6f7a6a 52%, var(--asphalt) 62%, var(--asphalt-dark) 100%);
  }
  .inset-frame {
    position: absolute;
    left: 61px;
    top: 61px;
    width: 1078px;
    height: 806px;
    border: 1.5px solid var(--frame);
    box-sizing: border-box;
  }
  .brand {
    position: absolute;
    left: 82px;
    top: 86px;
    display: flex;
    align-items: center;
    gap: 10px;
    font-family: "Roboto Condensed", sans-serif;
    font-weight: 700;
    font-size: 38px;
    line-height: 1;
    color: var(--brand-red);
    text-transform: uppercase;
  }
  .brand-mark {
    width: 18px;
    height: 18px;
    background: var(--brand-red);
  }
  .brand-name {
    display: flex;
    flex-direction: column;
    gap: 4px;
  }
  .headline {
    margin: 0;
    font-weight: normal;
  }
  .lead-in {
    position: absolute;
    left: 76px;
    top: 622px;
    font-family: "Roboto Condensed", sans-serif;
    font-weight: 400;
    font-size: 50px;
    line-height: 1;
    color: var(--ink);
    letter-spacing: -0.5px;
  }
  .experience {
    position: absolute;
    left: 95px;
    top: 676px;
    font-family: "Archivo Black", sans-serif;
    font-size: 48px;
    line-height: 1.1;
    color: var(--ink);
    letter-spacing: -1.5px;
    white-space: nowrap;
  }
  .experience .years {
    color: var(--accent);
  }
  .difference {
    position: absolute;
    left: 122px;
    top: 733px;
    font-family: "Oswald", sans-serif;
    font-weight: 200;
    font-size: 118px;
    line-height: 1;
    color: var(--frame);
    letter-spacing: 6px;
    white-space: nowrap;
  }
  .cta {
    position: absolute;
    left: 974px;
    top: 842px;
    font-family: "Oswald", sans-serif;
    font-weight: 700;
    font-size: 16px;
    line-height: 1;
    color: var(--accent);
    text-transform: uppercase;
    white-space: nowrap;
  }
</style>
</head>
<body>
  <main class="postcard">
    <div class="hero-photo" role="img" aria-label="Large white colonial house with grey roof among tall trees, green lawn, purple flowering clematis on a lamp post, and a freshly sealed curving asphalt driveway"></div>
    <div class="inset-frame"></div>

    <div class="brand">
      <span class="brand-mark"></span>
      <span class="brand-name"><span>Bellmont</span><span>Paving</span></span>
    </div>

    <h1 class="headline">
      <span class="lead-in">See why</span>
      <span class="experience"><span class="years">over 65 years</span> of experience</span>
      <span class="difference">MAKES A DIFFERENCE</span>
    </h1>

    <div class="cta">Contact us today</div>
  </main>
</body>
</html>
```